Self-Help Book Cover

This is a self-help book entitled, "Lanterns for Loners, Oddballs & Dreamers: A grounded and soulful guide to finding your footing among others."
I want the book cover to be primarily white, with red and black as secondary colors. I am open to cartoon interpretations of the words, "misfits, weirdos, and introverts" or a unique font used for each word. For the center, there can be white/gray people/balls with larger red people/balls in the middle of them shaped like an antique key. Or the center can be a red door that opens to a pleasant background image (maybe nature). This is just some ideas, I am open to others.
The author's name is Rosalind Whitcombe. The text on the back of the book is in a word doc file attached. I have also attached samples of the key and people/balls.
Updates
Requirements
Must have
- a .jpg or .tif(f) file
- at least 1000 pixels on the longest side
- ideal image height/width ratio is 1.6 (example: 1000 x 1600)
- The size should be 5.5" x 8.5"

```html
<!DOCTYPE html>
<html lang="en">
<head>
<meta charset="utf-8">
<title>Lanterns for Loners, Oddballs &amp; Dreamers — Cover</title>
<link rel="stylesheet" href="https://fonts.googleapis.com/css2?family=Bebas+Neue&family=Oswald:wght@300;400&family=Roboto+Condensed:wght@400&family=Montserrat:wght@600&family=Open+Sans:wght@400&display=swap">
<style>
  :root {
    --stage: #e4e5e7;
    --ink: #161616;
    --band-dark: #262829;
    --red: #c8161d;
    --red-band: #d0202a;
    --paper: #f3f3f3;
    --white: #ffffff;
    --spine: #2e3133;
  }
  * { box-sizing: border-box; margin: 0; padding: 0; }
  html, body { width: 1200px; height: 1200px; overflow: hidden; }
  body { background: var(--stage); position: relative; }

  .cover { position: absolute; top: 229px; height: 742px; overflow: hidden; }

  /* Front cover */
  .front { left: 80px; width: 480px; }
  .front-art {
    position: absolute; inset: 0;
    background:
      radial-gradient(ellipse 45% 40% at 52% 62%, rgba(255,236,190,0.95) 0%, rgba(214,170,100,0.55) 40%, rgba(90,80,60,0) 75%),
      radial-gradient(ellipse 60% 30% at 50% 85%, rgba(230,200,140,0.5) 0%, rgba(0,0,0,0) 70%),
      linear-gradient(180deg, #1f2a2c 0%, #3a4544 35%, #5b5a4e 65%, #3b3d3a 100%);
  }
  .front-title {
    position: absolute; top: 62px; left: 36px; right: 30px;
    color: var(--white);
  }
  .front-title .main {
    font-family: "Bebas Neue", sans-serif;
    font-size: 92px; line-height: 0.9; letter-spacing: 1px;
  }
  .front-title .sub {
    font-family: "Oswald", sans-serif; font-weight: 400;
    font-size: 31px; line-height: 1.1; letter-spacing: 0.5px; margin-top: 4px;
  }
  .front-title .tagline {
    display: block; margin-top: 8px; padding: 5px 8px;
    background: var(--red-band);
    font-family: "Roboto Condensed", sans-serif; font-size: 14.5px;
    color: var(--white); white-space: nowrap;
  }
  .author-band {
    position: absolute; left: 0; right: 0; bottom: 0; height: 66px;
    background: var(--band-dark);
    display: flex; flex-direction: column; align-items: center; justify-content: center;
  }
  .author-band::before {
    content: ""; width: 130px; height: 2px; background: #9a9a9a; margin-bottom: 10px;
  }
  .author-band .author {
    font-family: "Roboto Condensed", sans-serif; font-size: 17px;
    color: var(--white); letter-spacing: 0.5px; text-transform: uppercase;
  }

  /* Back cover */
  .back { left: 600px; width: 480px; background: var(--paper); }
  .back-art {
    position: absolute; left: 120px; top: 220px; width: 300px; height: 440px;
    background: radial-gradient(ellipse 50% 50% at 50% 55%, rgba(200,120,80,0.25) 0%, rgba(200,120,80,0) 70%);
  }
  .back-title { position: relative; text-align: center; padding-top: 54px; }
  .back-title .main {
    font-family: "Montserrat", sans-serif; font-weight: 600;
    font-size: 40px; color: var(--red); line-height: 1;
  }
  .back-title .sub {
    font-family: "Oswald", sans-serif; font-weight: 400;
    font-size: 26px; color: var(--ink); margin-top: 6px;
  }
  .back-title .rule {
    width: 150px; height: 2px; background: var(--red); margin: 6px auto 0;
  }
  .blurb {
    position: relative; margin: 22px 28px 0;
    font-family: "Open Sans", sans-serif; font-size: 13.2px; line-height: 1.42;
    color: var(--ink); text-align: justify;
  }
  .blurb p + p { margin-top: 8px; }

  /* Spine */
  .spine { left: 1080px; width: 40px; background: var(--spine); }
  .spine-title {
    position: absolute; left: 50%; top: 50%;
    transform: translate(-50%, -50%) rotate(-90deg);
    white-space: nowrap;
    font-family: "Oswald", sans-serif; font-weight: 400; font-size: 19px;
    color: var(--white); letter-spacing: 0.5px;
  }
</style>
</head>
<body>

<section class="cover front">
  <div class="front-art" role="img" aria-label="Misty photograph of a glowing keyhole doorway with a lone figure standing in the light"></div>
  <header class="front-title">
    <h1 class="main">LANTERNS FOR</h1>
    <div class="sub">LONERS, ODDBALLS &amp; DREAMERS</div>
    <span class="tagline">A Grounded And Soulful Guide To Finding Your Footing Among Others</span>
  </header>
  <footer class="author-band"><span class="author">Rosalind Whitcombe</span></footer>
</section>

<section class="cover back">
  <div class="back-art" role="img" aria-label="Faint warm-toned background image behind the blurb"></div>
  <header class="back-title">
    <div class="main">LANTERNS FOR</div>
    <div class="sub">LONERS, ODDBALLS &amp; DREAMERS</div>
    <div class="rule"></div>
  </header>
  <div class="blurb">
    <p>There are countless books out there on how to get ahead, but I have found that most of them make quiet assumptions about the people reading them – they picture a typical, outgoing, everyday reader. I would read those books and feel more lost than before, because they never touched the particular struggles I carried. Their advice only partly helped me find my way, and I grew up without the support or mentors that many of my peers enjoyed. I thought differently, hoped differently, and most of all, moved through the world differently from those around me. Still, I found my footing as a nurse, a translator, a teacher, and a writer. The greatest lesson of my life is that when you stand apart, your path must be different too.</p>
    <p>Perhaps you have spent years as a square peg pressed into a round hole. Few guides speak to your situation, and fewer people truly see you. We are taught to hide, to blend in, to smile at what confuses us. This is not a book about winning over a crowd; it is about learning to meet others as yourself.</p>
    <p>Your difference is a gift, and how you tend it will shape your life. This book offers practical steps and gentle reflection so that, in the end, every loner, oddball and dreamer can find a place to stand.</p>
  </div>
  <footer class="author-band"><span class="author">Rosalind Whitcombe</span></footer>
</section>

<section class="cover spine">
  <div class="spine-title">LANTERNS FOR LONERS, ODDBALLS &amp; DREAMERS</div>
</section>

</body>
</html>
```